Single Sided 1 Page Tour Flyer in the same theme as previous brochure

We need a single sided 8.5 x 11 flyer in the same theme and color scheme as the previous brochure we worked on together. the flyer should include the following

1. company logo up top (just like on the front panel of previous brochure
2. tour name "Maple & Pine Highlights" also on the top
3. a large photo towards the top of the flyer, similar to the brochure front
4. 3 panels of text: left one for tour prices, whats included, additional notes, center and right panels for tour program details (day 1, day 2, etc)
5. below that, a few lines for additional details, like small print and stuff
6. company address, phone numbers, email address, and website link
6. below that a banner of small photos, maybe 4 in a row, similar to the brochure

details of the actual tour can be found at this link:
http://bluepebbletrips.ru/en/tours/maple-and-pine-11-days/

once again, we would love for the flyer to be in the same theme and style as the other brochure, so it matches, we loved the previous work!!

```html
<!DOCTYPE html>
<html lang="en">
<head>
<meta charset="utf-8">
<title>Maple &amp; Pine Highlights – Tour Flyer</title>
<link href="https://fonts.googleapis.com/css2?family=Arimo:ital,wght@0,400;0,700;1,400;1,700&display=swap" rel="stylesheet">
<style>
  :root{
    --gold:#f2b705;
    --ink:#111111;
    --brand-grey:#6d6d6d;
    --panel:#ffffff;
    --panel-bg:#e6e6e6;
    --footer-dark:#0d0d0d;
    --footer-mid:#3a3a3a;
    --sky-top:#4f5f88;
    --sky-mid:#c98f84;
    --city-low:#2a2430;
  }
  *{box-sizing:border-box;margin:0;padding:0}
  html,body{width:927px;height:1200px;overflow:hidden;background:#fff}
  body{font-family:"Arimo",Arial,sans-serif;color:var(--ink)}
  .flyer{position:relative;width:927px;height:1200px;overflow:hidden;background:#fff}

  /* header */
  .brand{position:absolute;left:40px;top:46px;display:flex;align-items:center;gap:16px}
  .brand-dot{width:64px;height:64px;border-radius:50%;background:var(--gold)}
  .brand-name{font-size:40px;font-weight:400;color:var(--brand-grey);line-height:1}
  .tour-title{position:absolute;right:42px;top:38px;text-align:right;font-weight:700;line-height:1.12}
  .tour-title .line-1{display:block;font-size:44px;color:var(--ink)}
  .tour-title .line-2{display:block;font-size:44px;color:var(--gold)}

  /* hero */
  .hero{position:absolute;left:0;top:170px;width:927px;height:500px}
  .hero svg{display:block}

  /* content area */
  .content-bg{position:absolute;left:0;top:668px;width:927px;height:532px;background:linear-gradient(#f2f2f2,var(--panel-bg))}
  .footer-shape{position:absolute;left:0;top:860px;width:927px;height:340px}

  .panel{position:absolute;background:var(--panel);border-radius:12px;box-shadow:0 1px 4px rgba(0,0,0,.12)}
  .panel-price{left:33px;top:685px;width:288px;height:212px;padding:12px 16px}
  .panel-days-a{left:330px;top:685px;width:280px;height:322px;padding:11px 14px}
  .panel-days-b{left:614px;top:685px;width:295px;height:307px;padding:11px 14px}

  .price-lead{font-size:15px;font-weight:700;text-align:center;line-height:1.2}
  .price{font-size:50px;font-weight:700;text-align:center;line-height:1.1;letter-spacing:-1px}
  .price-note{font-size:8px;font-weight:700;margin-top:2px}
  .included-title{font-size:19px;font-weight:700;margin-top:14px;line-height:1}
  .included-list{list-style:none;margin-top:4px}
  .included-list li{font-size:8.5px;font-weight:700;line-height:1.3;padding-left:10px;position:relative}
  .included-list li::before{content:"";position:absolute;left:1px;top:3.5px;width:4px;height:4px;border-radius:50%;background:var(--ink)}
  .extra-notes{font-size:8.5px;font-weight:700;line-height:1.3;margin-top:10px}

  .itinerary-title{font-size:13px;font-weight:400;line-height:1.1}
  .itinerary-route{font-size:8.5px;font-weight:700;line-height:1.3}
  .day{margin-top:9px;font-size:8.3px;font-style:italic;line-height:1.3;color:#222}
  .day-first{margin-top:0}
  .day-label{font-weight:700;display:block}
  .footnote{font-size:7px;font-style:italic;line-height:1.3;margin-top:8px;color:#222}

  /* footer contacts */
  .contact{position:absolute;left:40px;color:var(--gold);font-size:12.5px;font-style:italic;line-height:1.45;display:flex;align-items:flex-start;gap:14px}
  .contact-icon{flex:none;width:22px;height:22px;margin-top:-1px;border-radius:50%;background:#fff;display:flex;align-items:center;justify-content:center}
  .contact-icon svg{display:block}
  .contact-address{top:1008px}
  .contact-phone{top:1074px}
  .contact-email{top:1122px}
  .contact-web{top:1154px}

  .thumb{position:absolute;border-radius:50%;border:3px solid #fff;box-shadow:0 2px 6px rgba(0,0,0,.35)}
  .thumb-monument{left:542px;top:1018px;width:110px;height:104px;background:radial-gradient(circle at 50% 35%,#dfe6ef,#8f9fb3)}
  .thumb-street{left:689px;top:1028px;width:158px;height:158px;background:radial-gradient(circle at 50% 40%,#8a86b8,#3b3a5c)}
</style>
</head>
<body>
<main class="flyer">

  <header>
    <div class="brand">
      <span class="brand-dot"></span>
      <span class="brand-name">BluePebble Trips</span>
    </div>
    <h1 class="tour-title">
      <span class="line-1">Maple &amp; Pine</span>
      <span class="line-2">Highlights</span>
    </h1>
  </header>

  <div class="hero">
    <svg width="927" height="500" viewBox="0 0 927 500">
      <defs>
        <linearGradient id="city-dusk" x1="0" y1="0" x2="0" y2="1">
          <stop offset="0" stop-color="var(--sky-top)"/>
          <stop offset="0.35" stop-color="#8f8aa4"/>
          <stop offset="0.55" stop-color="var(--sky-mid)"/>
          <stop offset="0.75" stop-color="#6c4e52"/>
          <stop offset="1" stop-color="var(--city-low)"/>
        </linearGradient>
      </defs>
      <rect x="0" y="0" width="927" height="500" fill="url(#city-dusk)" role="img" aria-label="Night skyline of a large city at dusk with a tall lit tower"/>
      <path d="M0 0 H927 V20 C760 -10 520 0 300 40 C180 62 80 70 0 62 Z" fill="#fff"/>
      <path d="M0 62 C120 72 260 40 420 28 C260 58 120 82 0 76 Z" fill="var(--gold)"/>
      <path d="M0 420 C180 460 420 488 620 478 C760 470 860 450 927 430 V500 H0 Z" fill="#fff"/>
      <path d="M300 462 C520 490 740 478 927 428 V448 C760 495 520 505 300 462 Z" fill="var(--gold)"/>
    </svg>
  </div>

  <div class="content-bg"></div>

  <svg class="footer-shape" width="927" height="340" viewBox="0 0 927 340" aria-hidden="true">
    <defs>
      <linearGradient id="footer-fade" x1="0" y1="0" x2="1" y2="0">
        <stop offset="0" stop-color="var(--footer-dark)"/>
        <stop offset="0.55" stop-color="#1c1c1c"/>
        <stop offset="1" stop-color="var(--footer-mid)"/>
      </linearGradient>
    </defs>
    <path d="M0 42 C150 32 300 70 420 135 C530 195 660 270 927 305 V340 H0 Z" fill="url(#footer-fade)"/>
    <path d="M0 30 C155 20 305 58 428 124 C540 186 670 258 927 292" fill="none" stroke="#bdbdbd" stroke-width="2"/>
    <path d="M0 18 C160 8 310 46 436 112" fill="none" stroke="#d6d6d6" stroke-width="1.5"/>
  </svg>

  <section class="panel panel-price">
    <p class="price-lead">Cost for 1 person starting from</p>
    <p class="price">$1,495</p>
    <p class="price-note">*Personalize in process of purchasing</p>
    <h2 class="included-title">Included in Price:</h2>
    <ul class="included-list">
      <li>Double occupancy in hotels along the route</li>
      <li>Breakfasts</li>
      <li>Excursions as per itinerary</li>
    </ul>
    <p class="extra-notes">Lorem ipsum dolor sit amet, consetetur sadipscing elitr, sed diam nonumy eirmod tempor invidunt ut labore et dolore magna aliquyam erat, sed diam voluptua.</p>
  </section>

  <section class="panel panel-days-a">
    <h2 class="itinerary-title">Tour Itinerary:</h2>
    <p class="itinerary-route">New York, Washington, D.C., Philadelphia, Boston, Montreal, Quebec, Ottawa, Niagara Falls.</p>
    <p class="day"><span class="day-label">Day 1</span>Arrival to Washington, D.C., registration in hotel. Overnight in Washington, D.C.</p>
    <p class="day"><span class="day-label">Day 2</span>Sightseeing tour of Washington, D.C.: memorials, Capitol Building, White House, museums, and much more. Overnight in Washington, D.C.</p>
    <p class="day"><span class="day-label">Day 3</span>Departure to Philadelphia. Sightseeing tour of Philadelphia. Departure to New York, leisure time in the evening. Overnight in New York</p>
    <p class="day"><span class="day-label">Day 4</span>Sightseeing tour of New York: Manhattan, Wall Street, United Nations Building, Broadway, Times Square. Overnight in N.Y. *Optional cruise to the Statue of Liberty and Ellis Island.</p>
    <p class="day"><span class="day-label">Day 5</span>Departure to Boston. Sightseeing tour of Boston, Harvard University. Overnight in Boston</p>
  </section>

  <section class="panel panel-days-b">
    <p class="day day-first"><span class="day-label">Day 6</span>Departure to Montreal, sightseeing tour of the city. Overnight in Montreal</p>
    <p class="day"><span class="day-label">Day 7</span>Sightseeing tour of Quebec, return to Montreal. Overnight in Montreal</p>
    <p class="day"><span class="day-label">Day 8</span>Second part of sightseeing tour of Montreal: Old Town, Montreal Port, Notre Dame de Montreal. Departure to Ottawa, sightseeing tour of Ottawa. Overnight in Ottawa</p>
    <p class="day"><span class="day-label">Day 9</span>Departure to Rockport, cruise of 1,000 Islands. Departure to Toronto. Overnight in Toronto</p>
    <p class="day"><span class="day-label">Day 10</span>Sightseeing tour of Toronto. Departure to Niagara Falls. Cruise to the Niagara Falls. Overnight in Niagara Falls</p>
    <p class="day"><span class="day-label">Day 11</span>Transfer to Toronto Airport (YYZ). End of tour program.</p>
    <p class="footnote">*We recommend extending your trip with additional nights in New York, for leisure time in Manhattan, Broadway shows, shopping, and much more</p>
  </section>

  <address class="contact contact-address">
    <span class="contact-icon"><svg width="10" height="12" viewBox="0 0 12 14"><path d="M6 0a5 5 0 0 0-5 5c0 4 5 9 5 9s5-5 5-9a5 5 0 0 0-5-5zm0 7a2 2 0 1 1 0-4 2 2 0 0 1 0 4z" fill="#333"/></svg></span>
    <span>Blue Pebble Trips, Inc.<br>4120 Harbor View Rd. Suite #310<br>Lakeside, CA 90417</span>
  </address>
  <div class="contact contact-phone">
    <span class="contact-icon"><svg width="8" height="12" viewBox="0 0 10 14"><rect x="1" y="0.5" width="8" height="13" rx="1.5" fill="none" stroke="#333" stroke-width="1.4"/><circle cx="5" cy="11" r="0.9" fill="#333"/></svg></span>
    <span>+1 (800) 555-0142<br>+1 (323) 555-0187</span>
  </div>
  <div class="contact contact-email">
    <span class="contact-icon"><svg width="12" height="9" viewBox="0 0 14 10"><rect x="0.5" y="0.5" width="13" height="9" rx="1" fill="#333"/><path d="M1 1l6 5 6-5" fill="none" stroke="#fff" stroke-width="1"/></svg></span>
    <span>info@bluepebbletrips.com</span>
  </div>
  <div class="contact contact-web">
    <span class="contact-icon"><svg width="12" height="12" viewBox="0 0 14 14"><circle cx="7" cy="7" r="6" fill="none" stroke="#333" stroke-width="1.4"/><circle cx="7" cy="7" r="2" fill="#333"/></svg></span>
    <span>www.bluepebbletrips.ru</span>
  </div>

  <div class="thumb thumb-monument" role="img" aria-label="Round photo of a statue monument against a pale sky"></div>
  <div class="thumb thumb-street" role="img" aria-label="Round photo of city street signs at a busy avenue at night"></div>

</main>
</body>
</html>
```